Private Optometric Practice Needs new Presentation Folders/Stationary

We recently moved our office and are looking to refresh our presentation folders and stationary. I tend to prefer simple, clean designs. We are a full scope optometric practice provide high quality eyewear, custom contact lenses, along with emergency care and treatment for dry eyes. We communicate with a lot of other doctors and want to exude professionalism. I have attached 2 versions of our logo.

Target Market(s)

Familys

Industry/Entity Type

Eyecare

Font styles to use
Sans Serif

Colors
0054AA
0677BA
7BADD7
CADEEF
E8F1F8

Requirements
Nice to have
• Bifold, areas to put information about practice, welcome letter

```html
<!DOCTYPE html>
<html lang="en">
<head>
<meta charset="utf-8">
<title>Clearview Optometry — Stationery</title>
<link href="https://fonts.googleapis.com/css2?family=Poppins:wght@400;500;600;700&display=swap" rel="stylesheet">
<style>
  :root {
    --navy: #0a1a26;
    --blue: #2e9fdc;
    --ink: #1c1c1c;
    --body: #3a3a3a;
    --paper: #ffffff;
    --window: #d9d9db;
    --window-ink: #8a8a8a;
    --bg-top: #f8f8f9;
    --bg-bottom: #e8e8ea;
  }
  * { box-sizing: border-box; margin: 0; padding: 0; }
  html, body { width: 1200px; height: 721px; overflow: hidden; }
  body {
    position: relative;
    font-family: 'Poppins', sans-serif;
    background: linear-gradient(180deg, var(--bg-top), var(--bg-bottom));
    color: var(--ink);
  }
  .sheet { position: absolute; box-shadow: 0 1px 4px rgba(0,0,0,.08); }

  /* Brand block (name set as plain text) */
  .brand { color: #fff; font-weight: 500; text-align: center; letter-spacing: .18em; line-height: 1.35; }
  .brand-dot { display: block; margin: 0 auto; border-radius: 50%; background: var(--blue); }
  .brand-tab {
    position: absolute; top: 0; background: var(--navy);
    display: flex; flex-direction: column; align-items: center; justify-content: center;
  }
  .rule { position: absolute; left: 0; right: 0; height: 1px; background: var(--blue); }

  /* Envelope */
  .envelope { left: 78px; top: 141px; width: 357px; height: 155px; background: var(--paper); }
  .envelope .rule { top: 19px; }
  .envelope .brand-tab { left: 20px; width: 42px; height: 29px; gap: 2px; }
  .envelope .brand { font-size: 3.6px; }
  .envelope .brand-dot { width: 7px; height: 7px; }
  .envelope-window {
    position: absolute; left: 21px; top: 80px; width: 99px; height: 56px;
    border-radius: 4px; background: linear-gradient(135deg, #e4e4e6, var(--window));
    border: 1px solid #cfcfd2; color: var(--window-ink); font-size: 5px;
  }
  .envelope-window .to { position: absolute; left: 11px; top: 19px; }
  .envelope-window .to b { color: #6a6a6a; font-weight: 600; }
  .envelope-window .addr { position: absolute; left: 20px; top: 28px; }

  /* Business cards */
  .card { width: 132px; height: 75px; top: 326px; background: var(--navy); }
  .card-front { left: 139px; display: flex; flex-direction: column; align-items: center; justify-content: center; gap: 4px; }
  .card-front .brand { font-size: 7px; }
  .card-front .brand-dot { width: 20px; height: 20px; }
  .card-back { left: 303px; }
  .card-back .brand { position: absolute; left: 10px; top: 31px; font-size: 4.4px; text-align: left; }
  .card-back .brand-dot { position: absolute; left: 16px; top: 17px; width: 11px; height: 11px; }
  .card-name { position: absolute; left: 54px; top: 22px; color: #fff; font-size: 4.2px; font-weight: 600; }
  .card-details { position: absolute; left: 54px; top: 31px; list-style: none; color: #d6dde3; font-size: 3px; line-height: 1.3; }
  .card-details li { display: flex; gap: 2px; align-items: flex-start; }
  .card-details svg { width: 3px; height: 3px; margin-top: .5px; flex: none; }

  /* Letterhead */
  .letter { left: 467px; top: 141px; width: 311px; height: 439px; background: var(--paper); font-size: 5.1px; color: var(--body); }
  .letter .rule { top: 29px; }
  .letter .brand-tab { left: 30px; width: 61px; height: 43px; gap: 3px; }
  .letter .brand { font-size: 5px; }
  .letter .brand-dot { width: 11px; height: 11px; }
  .letter p, .letter div.t { position: absolute; }
  .recipient { left: 34px; top: 91px; color: var(--ink); font-size: 5.5px; font-weight: 500; }
  .recipient-addr { left: 44px; top: 100px; }
  .letter-date { right: 33px; top: 92px; color: var(--ink); font-size: 5.5px; font-weight: 500; }
  .subject { left: 33px; top: 138px; line-height: 8.8px; }
  .subject-line { left: 33px; top: 174px; }
  .salutation { left: 33px; top: 192px; }
  .para { left: 33px; width: 246px; text-align: justify; line-height: 8.8px; }
  .para-1 { top: 209px; }
  .para-2 { top: 245px; }
  .closing { left: 33px; top: 332px; line-height: 8.8px; }
  .signature { left: 33px; top: 369px; color: var(--ink); font-weight: 600; }
  .footer-url {
    position: absolute; left: 0; right: 0; top: 427px;
    display: flex; justify-content: center; align-items: center; gap: 3px;
    font-size: 3.2px; color: #666;
  }
  .footer-url i { width: 3.5px; height: 3.5px; border-radius: 50%; background: var(--blue); display: block; }

  /* Folder */
  .folder { left: 811px; top: 141px; width: 311px; height: 439px; background: var(--navy); color: #fff; text-align: center; }
  .folder-brand { position: absolute; left: 0; right: 0; top: 29px; display: flex; flex-direction: column; align-items: center; gap: 4px; }
  .folder-brand .brand { font-size: 7px; }
  .folder-brand .brand-dot { width: 16px; height: 16px; }
  .folder-title { position: absolute; left: 0; right: 0; top: 199px; font-size: 15.5px; font-weight: 700; line-height: 1.02; }
  .folder-desc { position: absolute; left: 0; right: 0; top: 235px; font-size: 7.6px; }
  .folder .footer-url { color: #c7d0d8; }
  .folder .footer-url i { background: #c7d0d8; }
</style>
</head>
<body>

<section class="sheet envelope" aria-label="Envelope">
  <div class="rule"></div>
  <div class="brand-tab"><span class="brand-dot"></span><span class="brand">CLEARVIEW<br>OPTOMETRY</span></div>
  <div class="envelope-window">
    <p class="to"><b>To : Ms.</b> Partner</p>
    <p class="addr">123 Sample Address Here</p>
  </div>
</section>

<section class="sheet card card-front" aria-label="Business card front">
  <span class="brand-dot"></span>
  <span class="brand">CLEARVIEW<br>OPTOMETRY</span>
</section>

<section class="sheet card card-back" aria-label="Business card back">
  <span class="brand-dot"></span>
  <span class="brand">CLEARVIEW</span>
  <p class="card-name">DANIEL WHITFORD, O.D.</p>
  <ul class="card-details">
    <li><svg viewBox="0 0 10 10"><path d="M5 0a3.5 3.5 0 0 0-3.5 3.5C1.5 6 5 10 5 10s3.5-4 3.5-6.5A3.5 3.5 0 0 0 5 0z" fill="#2e9fdc"/></svg><span>1420 MAPLE GROVE AVE.<br>SUITE B<br>ASHFORD, MI 48000</span></li>
    <li><svg viewBox="0 0 10 10"><path d="M2 0l2 2.5-1.2 1.5a6 6 0 0 0 3.2 3.2L7.5 6 10 8l-1.5 2C4 10 0 6 0 1.5z" fill="#2e9fdc"/></svg><span>555-014-2290</span></li>
    <li><svg viewBox="0 0 10 10"><circle cx="5" cy="5" r="5" fill="#2e9fdc"/></svg><span>WWW.MYCLEARVIEWCARE.COM</span></li>
  </ul>
</section>

<section class="sheet letter" aria-label="Letterhead">
  <div class="rule"></div>
  <div class="brand-tab"><span class="brand-dot"></span><span class="brand">CLEARVIEW<br>OPTOMETRY</span></div>
  <p class="recipient">To : Ms. Partner</p>
  <p class="recipient-addr">123 Sample Address Here, City</p>
  <p class="letter-date">Date : January 04, 2021</p>
  <p class="subject">Sample Document Subject<br>Department Sample</p>
  <p class="subject-line">Here is the subject of the letter</p>
  <p class="salutation">Dear Ms. Partner,</p>
  <p class="para para-1">This is dummy text. It is only used to illustrate the gray value of the type. But is that really the case? Isn't it the same if I write "this is dummy text" or "Guaredisch nedunfeg"? Feguned – not at all.</p>
  <p class="para para-2">Dummy text provides important information, like the legibility of the body text, the impression it makes on the reader, the harmony between the individual figures, how narrow or wide they appear. Dummy text should contain as many different letters as possible and should be written in the original language. It doesn't have to make sense, it just needs to be readable. Texts in foreign languages, like "Lorem ipsum", don't actually serve this purpose, as they provide a false impression of what the body text actually looks like. This is dummy text. It is only used to illustrate the gray value of the type. But is that really the case? Isn't it the same if I write "this is dummy text" or "Guaredisch nedunfeg"? Feguned – not at all.</p>
  <p class="closing">Yours sincerely,<br>SAMPLE AG</p>
  <p class="signature">Clearview Optometry</p>
  <div class="footer-url"><i></i><span>WWW.MYCLEARVIEWCARE.COM</span></div>
</section>

<section class="sheet folder" aria-label="Presentation folder cover">
  <div class="folder-brand"><span class="brand-dot"></span><span class="brand">CLEARVIEW<br>OPTOMETRY</span></div>
  <h1 class="folder-title">YOUR DOCUMENT<br>TITLE HERE</h1>
  <p class="folder-desc">Description here</p>
  <div class="footer-url"><i></i><span>WWW.MYCLEARVIEWCARE.COM</span></div>
</section>

</body>
</html>
```